Tarjetas de visita para empresa de aluminio

Empresa con mas de 40 años vendiendo perfiles de aluminio.
Somos fábrica y almacén, queremos renovar la tarjeta de presentación de nuestros comerciales dando una imgen innovadora y tecnógica mezclado con la calidez del respeto al medio ambiente.
Añado el logo de la empresa y actual cara trasera de la tarjeta de visita, el logo es el simbolo ML y la marca TORVENIK EXTRUSION, la frase 2extrusion y lacado de aluminio" debe cambiarse por "Diseño, extrusión, lacado, anodizado y mecanizado de precisión de aluminio" o en su defecto incluir todos esos servicios que hacemos o una frase mas pegadiza.

We are an aluminium factory, we produce and stock profiles of aluminium.
we want to renew visit card of our sellers, we are looking for something that show innovation, tecnology and environment respect.
Upload our actual logo and back of visit card, logo ML and brand TORVENIK EXTRUSION must be keept.
Text "Extrusion y lacado de aluminio" must be changed for "Diseño, extrusion, lacado, anodizado y mecanizado de precisión de aluminio" or something like that

```html
<!DOCTYPE html>
<html lang="es">
<head>
<meta charset="utf-8">
<title>Torvenik Extrusion – Tarjetas de visita</title>
<link rel="stylesheet" href="https://fonts.googleapis.com/css2?family=Michroma&family=Arimo:wght@400;700&display=swap">
<style>
  :root {
    --backdrop: #e6e6e6;
    --card-front: #3b3b3d;
    --card-back: #2e2e30;
    --silver: #d9d9dc;
    --silver-dark: #8e8e92;
    --text-light: #f2f2f2;
    --text-muted: #c9c9cc;
    --rule: #a9a9ad;
  }
  * { box-sizing: border-box; margin: 0; padding: 0; }
  html, body { width: 1200px; height: 802px; overflow: hidden; }
  body {
    background: var(--backdrop);
    font-family: "Arimo", Arial, sans-serif;
    color: var(--text-light);
    position: relative;
  }
  .card {
    position: absolute;
    top: 221px;
    width: 560px;
    height: 360px;
    border-radius: 4px;
    overflow: hidden;
    box-shadow: 0 10px 24px rgba(0,0,0,.28);
  }
  /* ---------- front ---------- */
  .card--front { left: 30px; background: var(--card-front); }
  .front__silver-edge {
    position: absolute; left: 0; right: 0; bottom: 0; height: 16px;
    background: linear-gradient(180deg, var(--silver) 0%, #ffffff 45%, var(--silver-dark) 100%);
  }
  .front__brand-block {
    position: absolute; top: 26px; left: 0; right: 0;
    text-align: center;
  }
  .brand-mark {
    display: inline-block; width: 30px; height: 30px;
    border: 2px solid var(--silver); border-radius: 50%;
    margin-bottom: 8px;
  }
  .brand-name {
    font-family: "Michroma", sans-serif;
    font-size: 25px; letter-spacing: 2px;
    color: var(--silver);
  }
  .brand-tagline {
    font-family: "Michroma", sans-serif;
    font-size: 10.5px; letter-spacing: 2.4px;
    color: var(--text-muted); margin-top: 6px;
    text-transform: uppercase;
  }
  .person-name {
    font-weight: 700; font-size: 17px; letter-spacing: .5px;
    margin-top: 16px;
  }
  .person-role {
    display: inline-block; font-size: 12px; color: var(--text-muted);
    border-top: 1px solid var(--rule);
    padding-top: 3px; margin-top: 3px; min-width: 150px;
  }
  .front__divider {
    position: absolute; left: 30px; right: 30px; top: 212px;
    border-top: 1px solid var(--rule);
  }
  .contact-list {
    position: absolute; left: 30px; top: 226px; list-style: none;
    font-size: 12.5px; line-height: 19px;
  }
  .contact-list li { display: flex; align-items: center; gap: 9px; }
  .contact-list svg { width: 11px; height: 11px; flex: none; }
  .address {
    position: absolute; right: 30px; top: 226px;
    text-align: right; font-size: 12.5px; line-height: 19px;
  }
  .address__street { font-weight: 700; }
  /* ---------- back ---------- */
  .card--back { left: 610px; background: var(--card-back); }
  .back__pattern {
    position: absolute; inset: 0;
    background: linear-gradient(120deg, #262628 0%, #343436 55%, #5a5a5d 100%);
  }
  .back__info {
    position: absolute; left: 30px; right: 30px; bottom: 48px;
    display: flex; align-items: center; gap: 18px;
  }
  .back__text { flex: 1; text-align: center; }
  .back__headline { font-weight: 700; font-size: 15px; letter-spacing: .3px; }
  .back__services { font-weight: 700; font-size: 11.5px; margin-top: 6px; line-height: 15px; color: var(--text-muted); }
  .back__brand {
    display: flex; align-items: center; gap: 8px;
    font-family: "Michroma", sans-serif; font-size: 13px; color: var(--silver);
  }
  .back__brand .brand-mark { width: 22px; height: 22px; margin: 0; }
</style>
</head>
<body>
  <section class="card card--front" aria-label="Cara delantera">
    <div class="front__brand-block">
      <span class="brand-mark"></span>
      <div class="brand-name">TORVENIK EXTRUSION</div>
      <div class="brand-tagline">Extrusion y lacado de aluminio</div>
      <div class="person-name">ANDRÉS MOLINA CORTÉS</div>
      <div class="person-role">Comercial</div>
    </div>
    <div class="front__divider"></div>
    <ul class="contact-list">
      <li><svg viewBox="0 0 12 12"><rect x="3" y="0.5" width="6" height="11" rx="1" fill="none" stroke="#f2f2f2"/></svg>611 42 57 80</li>
      <li><svg viewBox="0 0 12 12"><path d="M2 1h3l1 3-2 1a7 7 0 0 0 3 3l1-2 3 1v3c-6 0-9-3-9-9z" fill="#f2f2f2"/></svg>954 28 17 46</li>
      <li><svg viewBox="0 0 12 12"><rect x="1" y="4" width="10" height="7" fill="#f2f2f2"/><rect x="3" y="1" width="6" height="4" fill="none" stroke="#f2f2f2"/></svg>954 28 17 47</li>
      <li><svg viewBox="0 0 12 12"><rect x="0.5" y="2.5" width="11" height="7" fill="none" stroke="#f2f2f2"/><path d="M1 3l5 4 5-4" fill="none" stroke="#f2f2f2"/></svg>andresmolina@torvenik.com</li>
      <li><svg viewBox="0 0 12 12"><circle cx="6" cy="6" r="5" fill="none" stroke="#f2f2f2"/><path d="M1 6h10M6 1c-3 3-3 7 0 10M6 1c3 3 3 7 0 10" fill="none" stroke="#f2f2f2"/></svg>www.torvenik.com</li>
    </ul>
    <div class="address">
      <div class="address__street">Pol.ind. Norvela - B4 Nº22</div>
      <div>41720 Villarreja Del</div>
      <div>Campo (Sevilla)</div>
      <div>Apartado De Correos 265</div>
    </div>
    <div class="front__silver-edge"></div>
  </section>

  <section class="card card--back" aria-label="Cara trasera">
    <div class="back__pattern" role="img" aria-label="Repetición en relieve del monograma de la empresa sobre fondo oscuro"></div>
    <div class="back__info">
      <div class="back__text">
        <div class="back__headline">Extrusion y lacado de aluminio</div>
        <div class="back__services">Diseño, extrusion, lacado, anodizado y mecanizado de<br>precisión de aluminio</div>
      </div>
      <div class="back__brand"><span class="brand-mark"></span>ML</div>
    </div>
  </section>
</body>
</html>
```